A Label for an ECO Friendly Spirit Company

Design a label which can be used for vodka and gin (London Dry Gin). It should be Square type Like the Shape File you see in the uploads. VORK means Local Eco friendly Authentic and Fair. We want a cool and slim label that calls for eco-friendly. We want to use it for our premium
Vodka and our London Dry Gin. Please use the logo and design it in Square Type.

40%vol, 700ml

Target Market(s)

spirits and events

Industry/Entity Type

SPIRITS

Colors
00AB8E
00BBA5
67D7C9
C6EFE9
E9F9F6
59FF00
82FF00
B8FF75
E3FFCB
F4FFEA

Requirements
Must have
• Logo from VORK, Squaee Shape

```html
<!DOCTYPE html>
<html lang="en">
<head>
<meta charset="utf-8">
<title>VORK Spirit Labels</title>
<link rel="stylesheet" href="https://fonts.googleapis.com/css2?family=Rye&family=Roboto+Slab:wght@700&family=Roboto+Mono:wght@700&display=swap">
<style>
  :root {
    --page-bg: #ffffff;
    --frame-light: #8dc63f;
    --frame-dark: #0b3a1c;
    --panel-deep: #052a16;
    --panel-mid: #5aa02e;
    --panel-bright: #7fcf2a;
    --art-bright: #86dc22;
    --art-mid: #4fb01a;
    --brand-teal: #00a389;
    --tagline-green: #8cc63f;
    --label-white: #ffffff;
  }
  html, body {
    margin: 0;
    width: 1200px;
    height: 1000px;
    overflow: hidden;
    background: var(--page-bg);
  }
  .canvas {
    position: relative;
    width: 1200px;
    height: 1000px;
  }
  .bottle-label {
    position: absolute;
    top: 229px;
    width: 517px;
    height: 517px;
  }
  .bottle-label--vodka { left: 65px; }
  .bottle-label--gin { left: 615px; }
  .brand-name {
    font-family: "Roboto Slab", serif;
    font-weight: 700;
    font-size: 34px;
    fill: var(--brand-teal);
    letter-spacing: 1px;
  }
  .brand-square { fill: var(--brand-teal); }
  .product-name {
    font-family: "Rye", serif;
    fill: var(--label-white);
    filter: drop-shadow(2px 3px 2px rgba(0, 0, 0, 0.45));
  }
  .tagline {
    font-family: "Roboto Slab", serif;
    font-weight: 700;
    font-size: 13px;
    letter-spacing: 2px;
  }
  .tagline--local { fill: var(--tagline-green); }
  .tagline--premium { fill: var(--brand-teal); }
  .spec {
    font-family: "Roboto Mono", monospace;
    font-weight: 700;
    font-size: 10px;
    fill: var(--label-white);
  }
</style>
</head>
<body>
<main class="canvas">

  <svg class="bottle-label bottle-label--vodka" viewBox="0 0 516 516" aria-label="VORK Vodka label">
    <defs>
      <linearGradient id="frameShade" x1="0" y1="0" x2="0" y2="1">
        <stop offset="0" stop-color="var(--frame-light)"/>
        <stop offset="0.5" stop-color="var(--frame-dark)"/>
        <stop offset="1" stop-color="var(--frame-light)"/>
      </linearGradient>
      <linearGradient id="panelShade" x1="0" y1="0" x2="0" y2="1">
        <stop offset="0.08" stop-color="var(--panel-deep)"/>
        <stop offset="0.2" stop-color="#0d4a20"/>
        <stop offset="0.36" stop-color="var(--panel-mid)"/>
        <stop offset="0.49" stop-color="var(--panel-bright)"/>
        <stop offset="0.64" stop-color="#58b81a"/>
        <stop offset="0.82" stop-color="#0f3f18"/>
        <stop offset="1" stop-color="var(--panel-deep)"/>
      </linearGradient>
      <linearGradient id="artShade" x1="0" y1="0" x2="0" y2="1">
        <stop offset="0" stop-color="var(--art-bright)" stop-opacity="0"/>
        <stop offset="0.25" stop-color="var(--art-bright)" stop-opacity="0.7"/>
        <stop offset="0.7" stop-color="var(--art-mid)" stop-opacity="0.7"/>
        <stop offset="1" stop-color="var(--art-mid)" stop-opacity="0"/>
      </linearGradient>
      <clipPath id="panelClip">
        <polygon points="258,29 487,258 258,487 29,258"/>
      </clipPath>
    </defs>
    <polygon class="label-frame" points="258,0 516,258 258,516 0,258" fill="url(#frameShade)"/>
    <polygon class="label-rule" points="258,24 492,258 258,492 24,258" fill="none" stroke="var(--frame-light)" stroke-width="2"/>
    <polygon class="label-panel" points="258,29 487,258 258,487 29,258" fill="url(#panelShade)"/>
    <rect class="leaf-art" role="img" aria-label="Large green leaf illustration behind the product name"
      x="29" y="195" width="458" height="225" fill="url(#artShade)" clip-path="url(#panelClip)"/>
    <rect class="brand-square" x="178" y="177" width="12" height="12"/>
    <text class="brand-name" x="264" y="201" text-anchor="middle">VORK</text>
    <text class="product-name" x="258" y="301" text-anchor="middle" font-size="74">VODKA</text>
    <text class="tagline tagline--local" x="258" y="369" text-anchor="middle">LOCAL AUTHENTIC</text>
    <text class="tagline tagline--premium" x="258" y="387" text-anchor="middle">PREMIUM</text>
    <text class="spec" x="258" y="426" text-anchor="middle">40%</text>
    <text class="spec" x="258" y="441" text-anchor="middle">Vol. 700ml</text>
  </svg>

  <svg class="bottle-label bottle-label--gin" viewBox="0 0 516 516" aria-label="VORK London Dry Gin label">
    <polygon class="label-frame" points="258,0 516,258 258,516 0,258" fill="url(#frameShade)"/>
    <polygon class="label-rule" points="258,24 492,258 258,492 24,258" fill="none" stroke="var(--frame-light)" stroke-width="2"/>
    <polygon class="label-panel" points="258,29 487,258 258,487 29,258" fill="url(#panelShade)"/>
    <rect class="leaf-art" role="img" aria-label="Large green leaf illustration behind the product name"
      x="29" y="195" width="458" height="225" fill="url(#artShade)" clip-path="url(#panelClip)"/>
    <rect class="brand-square" x="178" y="160" width="12" height="12"/>
    <text class="brand-name" x="264" y="184" text-anchor="middle">VORK</text>
    <text class="product-name" x="258" y="261" text-anchor="middle" font-size="56">LONDON</text>
    <text class="product-name" x="258" y="321" text-anchor="middle" font-size="56">DRY GIN</text>
    <text class="tagline tagline--local" x="258" y="369" text-anchor="middle">LOCAL AUTHENTIC</text>
    <text class="tagline tagline--premium" x="258" y="387" text-anchor="middle">PREMIUM</text>
    <text class="spec" x="258" y="426" text-anchor="middle">40%</text>
    <text class="spec" x="258" y="441" text-anchor="middle">Vol. 700ml</text>
  </svg>

</main>
</body>
</html>
```